Design a New Business Card for Our Company

We are looking for fresh, unique, and a modern business card that reflects our roots as digital marketing agency focused on SEM.

Industry/Entity Type

Marketing

Contact Information for Business Card

looking for very unique out of the box designs. clean and modern that compliments our logo

Requirements
Must have
• colors should match our logo
• Front should have name, address, email, and phone/fax of the person, phone/fax are the same number
• back should have our url

```html
<!DOCTYPE html>
<html lang="en">
<head>
<meta charset="utf-8">
<title>Northway Solutions – Business Card</title>
<link href="https://fonts.googleapis.com/css2?family=Mulish:wght@400;700&display=swap" rel="stylesheet">
<style>
  :root {
    --stage: #ed1c24;
    --card-dark: #262626;
    --card-light: #ffffff;
    --brand-blue: #5b93d3;
    --brand-grey: #b9b9b9;
    --text-grey: #9a9a9a;
    --url-grey: #cfcfcf;
  }
  * { margin: 0; padding: 0; box-sizing: border-box; }
  html, body {
    width: 1200px; height: 1000px; overflow: hidden;
    background: var(--stage);
    font-family: "Mulish", "Century Gothic", sans-serif;
  }
  .canvas { position: relative; width: 1200px; height: 1000px; }

  /* Back of card */
  .card-back {
    position: absolute; left: 234px; top: 117px;
    width: 588px; height: 335px;
    background: var(--card-dark);
    overflow: hidden;
  }
  .card-back__pattern {
    position: absolute; inset: 0;
    background:
      radial-gradient(circle at 85% 20%, rgba(255,255,255,0.05), transparent 35%),
      radial-gradient(circle at 10% 80%, rgba(255,255,255,0.05), transparent 35%);
  }
  .brand {
    position: absolute; display: flex; align-items: center;
  }
  .brand__dot {
    border-radius: 50%; background: var(--brand-blue); flex: none;
  }
  .brand__name {
    color: var(--brand-grey); font-weight: 700; white-space: nowrap;
    letter-spacing: -0.5px;
  }
  .card-back .brand { left: 110px; top: 132px; gap: 18px; }
  .card-back .brand__dot { width: 46px; height: 46px; }
  .card-back .brand__name { font-size: 40px; }
  .card-back__url {
    position: absolute; left: 0; right: 0; top: 260px;
    text-align: center; padding-left: 0;
    color: var(--url-grey); font-size: 19px; letter-spacing: 0.6px;
  }

  /* Front of card */
  .card-front {
    position: absolute; left: 392px; top: 553px;
    width: 574px; height: 328px;
    background: var(--card-light);
    overflow: hidden;
  }
  .person { position: absolute; left: 46px; top: 54px; }
  .person__name { color: var(--brand-blue); font-weight: 700; font-size: 28px; line-height: 1.1; }
  .person__role { color: var(--text-grey); font-size: 21px; margin-top: 4px; }

  .card-front .brand { left: 280px; top: 58px; gap: 10px; }
  .card-front .brand__dot { width: 26px; height: 26px; }
  .card-front .brand__name { font-size: 25px; }

  .contact-rail { position: absolute; left: 285px; top: 100px; width: 40px; height: 228px; }
  .contact-list { position: absolute; left: 332px; top: 0; list-style: none; color: var(--text-grey); font-size: 16px; }
  .contact-list li { position: absolute; left: 0; white-space: nowrap; line-height: 20px; }
</style>
</head>
<body>
<main class="canvas">

  <section class="card-back" aria-label="Card back">
    <div class="card-back__pattern" role="img" aria-label="Soft pattern of faint grey circles"></div>
    <div class="brand">
      <span class="brand__dot"></span>
      <span class="brand__name">Northway Solutions</span>
    </div>
    <p class="card-back__url">www.NorthwaySolutions.com</p>
  </section>

  <section class="card-front" aria-label="Card front">
    <div class="person">
      <h1 class="person__name">Alex Morgan</h1>
      <p class="person__role">Director</p>
    </div>

    <div class="brand">
      <span class="brand__dot"></span>
      <span class="brand__name">Northway Solutions</span>
    </div>

    <svg class="contact-rail" viewBox="0 0 40 228" aria-hidden="true">
      <line x1="18" y1="10" x2="18" y2="228" stroke="#5b93d3" stroke-width="3"/>
      <!-- fax -->
      <circle cx="18" cy="62" r="13" fill="#5b93d3"/>
      <rect x="12" y="57" width="12" height="9" rx="1.5" fill="none" stroke="#fff" stroke-width="1.6"/>
      <rect x="14" y="53" width="8" height="4" fill="#fff"/>
      <!-- phone -->
      <circle cx="18" cy="95" r="13" fill="#5b93d3"/>
      <path d="M11 93 q7 -6 14 0 l-2 2.5 h-2 l-1 -2 h-4 l-1 2 h-2 z M13.5 96 h9 v3.5 h-9 z" fill="#fff"/>
      <!-- mail -->
      <circle cx="18" cy="132" r="15" fill="#5b93d3"/>
      <rect x="10.5" y="126.5" width="15" height="11" rx="1" fill="#fff"/>
      <path d="M10.5 127 l7.5 6 l7.5 -6" fill="none" stroke="#5b93d3" stroke-width="1.3"/>
      <!-- pin -->
      <circle cx="18" cy="173" r="20" fill="#5b93d3"/>
      <path d="M18 184 c-5 -7 -7 -10 -7 -13 a7 7 0 0 1 14 0 c0 3 -2 6 -7 13 z" fill="#fff"/>
      <circle cx="18" cy="171" r="2.6" fill="#5b93d3"/>
    </svg>

    <ul class="contact-list">
      <li style="top:152px">0100 555 019</li>
      <li style="top:185px">0100 555 019</li>
      <li style="top:222px">alexmorgan@mail.com</li>
      <li style="top:255px">14 Harbor Lane,<br>Millbrook, NY 12500</li>
    </ul>
  </section>

</main>
</body>
</html>
```